Flyer-Design für ambulanten Pflegedienst (Essen auf Rädern)
Zielgruppe
Wir betreiben einen ambulanten Pflegedienst. Die Flyer sollen in den Haushalten verteilt werden.
Aufgabenstellung
Für das Essen auf Rädern soll eine Flyer in einem originellen Format entworfen werden. Der Flyer könnte in einem runden Format sein und sollte hochwertig wirken. Vielleicht ein hochweriget Teller mit einem gesunden essen darauf. u
Folgender Text sollte enthalten sein:
Logo bitte der Homepage www.Kavuro.de entnehmen
Text auf dem neuen Flyer
Wenn Sie einen Pflegegrad haben, liefern wir Ihnen das Essen auf Rädern nach Hause

```html
<!DOCTYPE html>
<html lang="de">
<head>
<meta charset="utf-8">
<title>Kavuro – Essen auf Rädern</title>
<link rel="stylesheet" href="https://fonts.googleapis.com/css2?family=Roboto+Slab:wght@700;800&display=swap">
<style>
  :root {
    --backdrop: #2a2a2a;
    --ring-green: #8cc63f;
    --ring-green-soft: #b7dc84;
    --paper: #ffffff;
    --headline-red: #b3162e;
    --tag-paper: #efe7d4;
    --tag-edge: #d9ccb0;
    --ink: #2a2320;
    --string: #7a5a3c;
  }
  html, body {
    margin: 0;
    padding: 0;
    width: 1200px;
    height: 1200px;
    overflow: hidden;
    background: var(--backdrop);
  }
  .flyer {
    display: block;
    width: 1200px;
    height: 1200px;
    font-family: "Roboto Slab", Georgia, serif;
  }
  .flyer-disc { fill: var(--paper); stroke: var(--ring-green); stroke-width: 28; }
  .inner-ring { fill: none; stroke: var(--ring-green-soft); stroke-width: 3; }
  .motion-line { fill: none; stroke: var(--ring-green); stroke-width: 6; stroke-linecap: round; }
  .headline { fill: var(--headline-red); font-weight: 800; font-size: 52px; }
  .tag-shape { fill: var(--tag-paper); stroke: var(--tag-edge); stroke-width: 2; }
  .tag-hole { fill: var(--paper); stroke: #b9a98a; stroke-width: 3; }
  .tag-string { fill: none; stroke: var(--string); stroke-width: 3; stroke-linecap: round; }
  .tag-address { fill: var(--ink); font-weight: 700; font-size: 26px; }
  .tag-web { fill: var(--headline-red); font-weight: 800; font-size: 34px; }
  .tag-mail { fill: var(--ink); font-weight: 700; font-size: 24px; }
  .brand-name { fill: var(--headline-red); font-weight: 800; font-size: 50px; letter-spacing: 2px; }
  .brand-square { fill: var(--headline-red); }
</style>
</head>
<body>
<svg class="flyer" viewBox="0 0 1200 1200" xmlns="http://www.w3.org/2000/svg">
  <defs>
    <radialGradient id="plateTones" cx="50%" cy="50%" r="50%">
      <stop offset="0%" stop-color="#e9a064"/>
      <stop offset="45%" stop-color="#c9b48a"/>
      <stop offset="80%" stop-color="#f2f2f0"/>
      <stop offset="100%" stop-color="#dedede"/>
    </radialGradient>
    <path id="headlineArcOuter" d="M150,592 A450,450 0 0 1 989.7,367"/>
    <path id="headlineArcInner" d="M202,606 A398,398 0 0 1 951,405"/>
  </defs>

  <!-- round flyer -->
  <circle class="flyer-disc" cx="600" cy="600" r="568"/>
  <circle class="inner-ring" cx="600" cy="600" r="528"/>

  <!-- motion lines -->
  <path class="motion-line" d="M175,700 A440,440 0 0 0 245,860"/>
  <path class="motion-line" d="M205,690 A410,410 0 0 0 265,830"/>
  <path class="motion-line" d="M140,760 A470,470 0 0 0 230,930"/>
  <path class="motion-line" d="M1020,420 A440,440 0 0 1 1045,560"/>
  <path class="motion-line" d="M995,440 A410,410 0 0 1 1012,540"/>
  <path class="motion-line" d="M880,980 A440,440 0 0 0 960,900"/>

  <!-- plate with meal -->
  <circle cx="600" cy="592" r="352" fill="url(#plateTones)" role="img" aria-label="Weißer Teller mit gegrillter Hähnchenbrust und buntem Gemüse: Brokkoli, Blumenkohl, Karotten, Paprika und Zuckerschoten"/>

  <!-- headline on arc -->
  <text class="headline">
    <textPath href="#headlineArcOuter" textLength="1150" lengthAdjust="spacing">Wenn Sie einen Pflegegrad haben, liefern wir</textPath>
  </text>
  <text class="headline">
    <textPath href="#headlineArcInner" textLength="1060" lengthAdjust="spacing">Ihnen das Essen auf Rädern nach Hause</textPath>
  </text>

  <!-- contact tag -->
  <g class="contact-tag" transform="translate(680,680) rotate(-12)">
    <path class="tag-shape" d="M0,0 H330 L410,55 V170 L330,225 H0 Z"/>
    <circle class="tag-hole" cx="372" cy="112" r="11"/>
    <path class="tag-string" d="M372,112 C410,90 440,80 470,95"/>
    <text class="tag-address" x="26" y="42">Kavuro Der mobile</text>
    <text class="tag-address" x="26" y="74">Pflegdienst GmbH</text>
    <text class="tag-address" x="26" y="106">Lindenweg 12</text>
    <text class="tag-address" x="26" y="138">17168 Bergfeld</text>
    <text class="tag-web" x="26" y="182">www.Kavuro.de</text>
    <text class="tag-mail" x="26" y="212">info@kavuro.de</text>
  </g>

  <!-- brand -->
  <g class="brand">
    <rect class="brand-square" x="468" y="968" width="34" height="34"/>
    <text class="brand-name" x="520" y="1003">Kavuro</text>
  </g>
</svg>
</body>
</html>
```